Business card logo/design needed

I need a new and fresh business card to get my name out there.
I have made plenty before and have a logo but I dont think it is sending the right message across.
I am a personal trainer running a small online business designed to cut the cost of training by taking it online, allowing you to purchase training over the net, through the help of Skype and video uploads.
You can personalized programs hand written for you or more general programs aimed at your goals.
Our goal is to get everyone to look like and behave like an athlete because there is no point in being in shape if you cant do anything with that body.
I also have a strong background in sports, having played low level college basketball in america and worked as a strength and conditioning coach. I dont like running or slow cardio, I am more focused on weights and functional training for aerobic fitness.
I am young for what I do, but I have lot of knowledge and I need something that says that I am not your standard drill sergeant trainer but someone who will truly help you reach your goals.
My curent logo text is "the steps to greatness" but I am not set on that.

Industry/Entity Type

Personal Trainer

Contact Information for Business Card

Corwin Maddock
Ironvale Motion
Personal trainer
Strength and conditioning coach
0491 572 806
www.ironvalemotion.com

```html
<!DOCTYPE html>
<html lang="en">
<head>
<meta charset="utf-8">
<title>Ironvale Motion – Business Card</title>
<link rel="stylesheet" href="https://fonts.googleapis.com/css2?family=Jost:wght@300;400;600;700&display=swap">
<style>
  :root {
    --canvas-bg: #ffffff;
    --frame-line: #1a1a1a;
    --green-deep: #0b5400;
    --green-mid: #2f8a00;
    --green-bright: #99ff00;
    --ink: #111111;
    --logo-ink: #ffffff;
  }
  html, body {
    margin: 0;
    padding: 0;
    width: 1200px;
    height: 1000px;
    overflow: hidden;
    background: var(--canvas-bg);
  }
  .stage {
    position: relative;
    width: 1200px;
    height: 1000px;
    box-sizing: border-box;
    border: 2px solid var(--frame-line);
    font-family: "Jost", "Century Gothic", sans-serif;
  }
  .card {
    position: absolute;
    left: 220px;
    top: 247px;
    width: 770px;
    height: 444px;
    background:
      radial-gradient(ellipse 520px 420px at 610px 323px,
        var(--green-bright) 0%,
        #6fd400 22%,
        #46a800 48%,
        var(--green-mid) 75%,
        var(--green-deep) 100%);
    overflow: hidden;
  }
  .brand {
    position: absolute;
    left: 60px;
    top: 44px;
    margin: 0;
    font-size: 54px;
    font-weight: 600;
    line-height: 1;
    color: var(--logo-ink);
    letter-spacing: 1px;
  }
  .details {
    position: absolute;
    left: 381px;
    top: 188px;
    color: var(--ink);
  }
  .person-name {
    margin: 0;
    font-size: 30px;
    line-height: 1;
    letter-spacing: 6px;
  }
  .person-name .first { font-weight: 700; }
  .person-name .last { font-weight: 300; }
  .roles {
    margin: 12px 0 0;
    font-size: 19px;
    font-weight: 400;
    line-height: 26px;
  }
  .contact {
    margin: 50px 0 0;
    font-size: 20px;
    font-weight: 700;
    line-height: 31px;
  }
</style>
</head>
<body>
  <div class="stage">
    <section class="card">
      <h1 class="brand">Ironvale Motion</h1>
      <div class="details">
        <p class="person-name"><span class="first">Corwin</span> <span class="last">Maddock</span></p>
        <p class="roles">Personal trainer<br>Strength and conditioning coach</p>
        <p class="contact">0491 572 806<br>www.ironvalemotion.com</p>
      </div>
    </section>
  </div>
</body>
</html>
```